Backup Software Tri-fold Brochure Project

We need a great looking and informative brochure to describe our new Backup Software offering. The brochures are to be used in retail and small business environments given to clients interested in protecting their computer from data loss.
The brochure should include attractive imagery that conveys a sense of Trust and Security to the prospective client.
The copy is provided as an attachment to this project. We'd like our Bright Deskpoint product logo to be printed on the back cover. The logo is attached to this project.
The finished tri-fold brochure will be submitted to Plumcopy for printing as an 8.5" x 11" tri-fold brochure. Their design instructions are online http://plumcopy-example.com/custom-brochures.aspx.
The finished product should be Adobe Illustrator CS3 (*.ai) with a PDF Proof.
Target Market(s)
Retail and Small Business customers
Industry/Entity Type
Software
Designer to choose colors to be used in the design.

```html
<!DOCTYPE html>
<html lang="en">
<head>
<meta charset="utf-8">
<title>Bright Deskpoint – Backup Tri-fold Brochure</title>
<link rel="stylesheet" href="https://fonts.googleapis.com/css2?family=Exo+2:wght@400;600;700&family=Open+Sans:wght@300;400;600;700&display=swap">
<style>
  :root {
    --blue: #1d5fa6;
    --blue-dark: #17498a;
    --navy: #0b2a63;
    --green: #6cb33f;
    --ink: #222;
    --paper: #f7f7f7;
    --backdrop: #2b2b2b;
  }
  * { box-sizing: border-box; margin: 0; padding: 0; }
  html, body { width: 776px; height: 1200px; overflow: hidden; background: var(--backdrop); }
  .stage { width: 776px; height: 1200px; position: relative; overflow: hidden; }
  .artboard { position: absolute; left: 0; top: 0; width: 900px; height: 1392px; transform: scale(0.86222); transform-origin: 0 0; }
  .sheet { position: absolute; left: 57px; width: 792px; height: 612px; overflow: hidden; font-family: "Open Sans", sans-serif; }
  .sheet--outside { top: 64px; background: var(--paper); }
  .sheet--inside { top: 714px; background: radial-gradient(ellipse at 55% 35%, #2d6fd0 0%, #174a9c 45%, var(--navy) 100%); color: #fff; }
  .abs { position: absolute; }
  .wave { position: absolute; left: 0; top: 0; width: 792px; height: 612px; }

  /* outside */
  .panel-tint { position: absolute; top: 0; width: 264px; height: 612px; }
  .panel-tint--left { left: 0; background: linear-gradient(90deg, #fff, #efefef); }
  .panel-tint--mid { left: 264px; background: #f4f4f4; }
  .panel-tint--right { left: 528px; background: linear-gradient(90deg, #fdfdfd, #eeeeee); }
  .kicker { font-family: "Exo 2", sans-serif; font-weight: 600; color: var(--blue); }
  .rule { position: absolute; height: 1px; background: var(--green); }
  .body-copy { font-size: 9px; line-height: 12.2px; text-align: justify; color: var(--ink); }
  .body-copy p + p { margin-top: 10px; }
  .slogan { font-family: "Exo 2", sans-serif; font-weight: 700; font-size: 24px; line-height: 30px; color: #fff; }
  .centered { text-align: center; }
  .fact-list { list-style: none; font-size: 11px; line-height: 19.5px; color: var(--ink); }
  .brand { display: flex; align-items: center; justify-content: center; gap: 8px; font-family: "Exo 2", sans-serif; font-weight: 700; color: var(--blue-dark); }
  .brand-mark { width: 30px; height: 30px; background: var(--green); flex: none; }
  .cta { font-family: "Exo 2", sans-serif; font-weight: 600; font-size: 14.5px; line-height: 17.5px; color: var(--ink); }
  .phone { font-family: "Exo 2", sans-serif; font-weight: 600; font-size: 27px; }
  .sources { font-size: 10.5px; line-height: 14px; color: var(--blue); }
  .sources p + p { margin-top: 5px; }
  .copyright { font-size: 7.5px; line-height: 13px; color: var(--ink); }
  .web { font-size: 17px; color: #fff; }
  .headline { font-family: "Exo 2", sans-serif; font-weight: 700; text-align: center; }
  .photo { position: absolute; }
  .call-now { font-family: "Exo 2", sans-serif; font-weight: 600; color: #fff; text-align: right; }

  /* inside */
  .col-title { font-size: 21px; line-height: 23px; font-weight: 300; }
  .col-title strong { color: var(--green); font-weight: 700; }
  .inside-copy { font-size: 9px; line-height: 12.3px; text-align: justify; color: #fff; }
  .inside-copy p + p { margin-top: 10px; }
  .todo { font-size: 13.5px; line-height: 19px; font-weight: 700; }
  .todo em { font-style: normal; color: var(--green); }
  .options-title { font-size: 18px; font-weight: 400; }
  .options { font-size: 11px; line-height: 15px; }
  .options .lead { color: var(--green); font-weight: 600; font-size: 11.5px; }
  .options strong { color: var(--green); font-weight: 600; }
  .options p + p { margin-top: 11px; }
  .circle { position: absolute; border-radius: 50%; border: 7px solid var(--green); }
</style>
</head>
<body>
<div class="stage">
 <div class="artboard">

  <!-- Outside spread -->
  <section class="sheet sheet--outside">
    <div class="panel-tint panel-tint--left"></div>
    <div class="panel-tint panel-tint--mid"></div>
    <div class="panel-tint panel-tint--right"></div>

    <div class="photo" role="img" aria-label="Photo of a frustrated businessman at a laptop" style="left:528px;top:256px;width:264px;height:270px;background:linear-gradient(160deg,#d9dde2 0%,#9aa3ad 45%,#3b4652 100%);"></div>

    <svg class="wave" viewBox="0 0 792 612" aria-hidden="true">
      <path d="M0 406 C 150 450 300 505 420 522 C 560 532 680 516 792 500 L792 612 L0 612 Z" fill="#1d5fa6"/>
      <path d="M0 406 C 150 450 300 505 420 522 C 560 532 680 516 792 500 L792 612 L0 612 Z" fill="#17498a" opacity="0.35"/>
      <path d="M240 512 C 420 540 630 522 792 462 L792 482 C 630 540 420 552 240 512 Z" fill="#6cb33f"/>
      <path d="M0 406 C 150 450 260 492 360 514 C 250 500 140 468 0 418 Z" fill="#ffffff" opacity="0.8"/>
    </svg>

    <!-- left panel -->
    <h2 class="kicker abs" style="left:28px;top:24px;width:220px;font-size:15px;line-height:21px;">YOUR ENTIRE DIGITAL LIFE<br>IS AT RISK</h2>
    <div class="rule" style="left:28px;top:69px;width:88px;"></div>
    <div class="body-copy abs" style="left:28px;top:84px;width:224px;">
      <p>Your computer stores everything you've ever created. Everything you've written, every email you've sent, every list you've made, every picture you've taken or movie you've made, all music you've created, your proposals, your spreadsheets, your presentations, your word files, your artwork, programs you've written, anything you've dictated, and much more... All your digital life is stored on your computer and is at risk of loss without backup.</p>
      <p>And your computer stores a copy of all your personal information. Your passwords, your online banking, your PINs, your credit cards and all your health and shopping records. This makes it a juicy target for hackers. Every day your digital life is exposed to computer Viruses, Malware and spammers all trying to break in. If they succeed the damage could be incalculable.</p>
      <p>If hackers destroy your information or a simple hard drive failure happens, restoring your programs will cost you days of effort and potentially hundreds of dollars. But your files could be unrecoverable. This means the loss of everything you've ever created.</p>
    </div>
    <p class="slogan abs" style="left:28px;top:503px;">The Only<br>Protection is a<br>GREAT BACKUP.</p>

    <!-- middle panel -->
    <h2 class="kicker abs centered" style="left:264px;top:34px;width:264px;font-size:21px;">DID YOU KNOW?</h2>
    <div class="rule" style="left:352px;top:68px;width:88px;"></div>
    <p class="abs centered" style="left:264px;top:84px;width:264px;font-size:16px;font-weight:600;color:var(--ink);">Every Week (in the US)</p>
    <ul class="fact-list abs centered" style="left:264px;top:112px;width:264px;">
      <li>* 140,000 drives crash</li>
      <li>* 12,000 laptops are lost or stolen</li>
      <li>* 37,000 Internet Crimes are committed</li>
      <li>* Internet criminals steal $25 Million</li>
    </ul>
    <div class="brand abs" style="left:264px;top:218px;width:264px;font-size:19px;"><span class="brand-mark"></span>Bright Deskpoint</div>
    <p class="cta abs centered" style="left:264px;top:280px;width:264px;">CALL US TO SCHEDULE<br>A DAY TO BRING IN<br>YOUR COMPUTER.</p>
    <p class="phone abs centered" style="left:264px;top:332px;width:264px;color:var(--ink);">0123 456 789</p>
    <div class="sources abs centered" style="left:274px;top:378px;width:244px;">
      <p>http://www.notebook-survey-example.com/<br>lost_laptop_study.pdf</p>
      <p>http://research.drivelab-example.com/<br>disk_failures.pdf</p>
      <p>https://www.netcrime-report-example.org/<br>2016_Report.pdf</p>
    </div>
    <p class="copyright abs centered" style="left:264px;top:478px;width:264px;">Copyright(c) 2017, Lanterra Systems, Inc.<br>All Rights Reserved</p>
    <p class="web abs centered" style="left:264px;top:572px;width:264px;">www.yourweb.com</p>

    <!-- right panel -->
    <div class="brand abs" style="left:528px;top:44px;width:264px;font-size:23px;"><span class="brand-mark" style="width:34px;height:34px;"></span>Bright Deskpoint</div>
    <div class="headline abs" style="left:528px;top:128px;width:264px;">
      <p style="font-size:27px;line-height:31px;color:var(--blue);">YOUR ENTIRE</p>
      <p style="font-size:27px;line-height:31px;"><span style="color:var(--green);">DIGITAL LIFE</span> <span style="color:var(--blue);">IS</span></p>
      <p style="font-size:36px;line-height:40px;color:var(--blue-dark);">AT RISK!</p>
    </div>
    <div class="call-now abs" style="left:528px;top:546px;width:232px;">
      <p style="font-size:21px;line-height:24px;">CALL NOW</p>
      <p style="font-size:27px;line-height:29px;">0123 456 789</p>
    </div>
  </section>

  <!-- Inside spread -->
  <section class="sheet sheet--inside">
    <svg class="wave" viewBox="0 0 792 612" aria-hidden="true">
      <path d="M0 555 C 300 555 560 520 792 432 L792 612 L0 612 Z" fill="#6cb33f"/>
      <path d="M0 548 C 300 548 560 512 792 424 L792 434 C 560 522 300 557 0 557 Z" fill="#ffffff"/>
    </svg>

    <div role="img" aria-label="Illustration of large blue 3D letters spelling BACKUP with a computer mouse attached by a cable" style="position:absolute;left:310px;top:350px;width:470px;height:230px;background:radial-gradient(ellipse at 50% 55%,rgba(80,180,240,0.75) 0%,rgba(40,130,210,0.45) 45%,rgba(20,80,170,0) 75%);"></div>

    <div class="circle" role="img" aria-label="Illustration of a cloud labeled Backup with a pointing hand cursor" style="left:33px;top:344px;width:116px;height:116px;background:radial-gradient(circle,#f4f8fc,#c9dff2);"></div>
    <div class="circle" role="img" aria-label="Photo of a stressed young man at a desk with a coffee mug" style="left:131px;top:374px;width:150px;height:150px;background:linear-gradient(160deg,#e8e2d8,#b9a58e 60%,#7a6a58);"></div>
    <div class="circle" role="img" aria-label="Illustration of a laptop with disaster recovery plan icons" style="left:38px;top:456px;width:140px;height:140px;background:radial-gradient(circle,#e23b3b,#b51f25);"></div>

    <!-- column 1 -->
    <h2 class="col-title abs" style="left:30px;top:24px;">WE HAVE<br><strong>WHAT YOU NEED</strong></h2>
    <div class="inside-copy abs" style="left:30px;top:82px;width:226px;">
      <p>We can create a snapshot of all the programs and files on your computer using our Image Backup technology. We'll give you your backup on an external hard drive which you can store someplace safe. If anything happens, just bring in your computer and your Image Backup and we'll restore your computer back to the point when the snapshot was taken.</p>
      <p>Restoring from an Image Backup is like setting your computer back in time. To make sure all your new files are protected, we'll also install Lanterra Systems' Bright Deskpoint software to backup your files every night. These backups are stored in Lanterra Systems' secure datacenter to protect you from even the most severe data loss scenarios.</p>
      <p>The combination of your Image Backup and your nightly backup will ensure you have complete protection for both your programs and your files. It means complete peace of mind.</p>
    </div>

    <!-- column 2 -->
    <h2 class="col-title abs" style="left:297px;top:24px;">HOW IT <strong>WORKS</strong></h2>
    <div class="inside-copy abs" style="left:297px;top:62px;width:198px;">
      <p>Our technology is designed to take advantage of the powerful imaging technology embedded in Corvane OS. Deep within the core of the OS is an imaging engine that can create a point-in-time backup of the Corvane OS system, device drivers, programs and system state. The backup can be used later to recover the system back to this point-in-time.</p>
      <p>Backups created by our Imaging technology can even be used to restore Corvane OS to dissimilar hardware. This is a quick way to migrate to a new computer without having to reinstall everything from scratch.</p>
      <p>Our technology stores backups as Corvane "Virtual Hard Disk" (VHD). These VHD files can be directly mounted from the Corvane OS Disk Manager. This is a great way to browse the contents of your Image Backup and restore individual files and folders.</p>
    </div>

    <!-- column 3 -->
    <h2 class="col-title abs" style="left:560px;top:24px;">WHAT <strong>TO DO</strong></h2>
    <p class="todo abs" style="left:560px;top:64px;width:215px;">Once a month we do <em>"Image Backup Saturday"</em>. Drop off your computer in the morning and pick it up a few hours later. <em>CALL FOR A COPY OF OUR SCHEDULE.</em></p>
    <h3 class="options-title abs" style="left:560px;top:190px;">OPTIONS</h3>
    <div class="options abs" style="left:560px;top:224px;width:215px;">
      <p class="lead">Our Image Backup technology<br>can protect</p>
      <p>Corvane OS PC's and Laptops running Corvane OS 7 and above <strong>(Corvane OS 8, 10+)</strong></p>
      <p>Corvane OS Servers running Corvane OS 2008 and above <strong>(Corvane OS 2012, 2016+)</strong></p>
    </div>
  </section>

 </div>
</div>
</body>
</html>
```